Business Card Design

Cake decorating business in a small town in Australia. looking for a style that is fresh with a touch of vintage/country. liking these ideas, timber backgrounds, chalkboards, bunting, flowers and cake elements (rolling pins, cupcakes, cake stands, etc.) would consider a shot saying/statement. would like the back of the card to have wording "Specialising in delectable treats for all your special occasions" - wedding cakes - birthday cakes - special occasion cakes - novelty cakes - cupcakes, cookies, slices and cake pops. maybe incorporate a cake in design on back page. attached are a few of my favourite cakes and the start of a card design I liked.

Industry/Entity Type

Business

Contact Information for Business Card

Marigold's Sugarloft Bakes 0438 056 969Find me on (Chirpwall Logo)

Requirements
Nice to have
• timber, some of my designs, chalkboard, baking utensils
Should not have
• no red font

```html
<!DOCTYPE html>
<html lang="en">
<head>
<meta charset="utf-8">
<title>Marigold's Sugarloft Bakes – Business Card</title>
<link rel="stylesheet" href="https://fonts.googleapis.com/css2?family=Lobster&family=Dancing+Script:wght@500&family=Roboto:wght@500&display=swap">
<style>
  :root {
    --stage: #2b2b2d;
    --timber-a: #cbc6bd;
    --timber-b: #b9b3aa;
    --timber-c: #d6d1c8;
    --timber-d: #aea89f;
    --timber-grain: rgba(110,104,96,.18);
    --timber-seam: #6e6962;
    --chalk: #313133;
    --chalk-line: #d9d6cf;
    --pink: #e98a93;
    --pink-deep: #d96f7b;
    --cream: #fbf8f1;
    --ink: #3a3532;
    --photo-warm-a: #c98d62;
    --photo-warm-b: #8d9a9c;
    --photo-cream-a: #e9e2b8;
    --photo-cream-b: #8c7b6a;
  }
  * { box-sizing: border-box; margin: 0; padding: 0; }
  html, body {
    width: 1200px; height: 800px; overflow: hidden;
    background: var(--stage);
  }
  .canvas {
    position: relative; width: 1200px; height: 800px;
    display: flex; align-items: center; justify-content: center; gap: 40px;
  }
  .card {
    position: relative; width: 540px; height: 310px;
    border-radius: 22px; overflow: hidden;
    box-shadow: 0 14px 30px rgba(0,0,0,.45);
  }

  /* Front – vertical timber planks */
  .card-front {
    background:
      repeating-linear-gradient(90deg,
        transparent 0 52px, var(--timber-seam) 52px 54px),
      repeating-linear-gradient(90deg,
        transparent 0 9px, var(--timber-grain) 9px 10px, transparent 10px 23px,
        var(--timber-grain) 23px 24px, transparent 24px 37px),
      repeating-linear-gradient(90deg,
        var(--timber-a) 0 54px, var(--timber-b) 54px 108px,
        var(--timber-c) 108px 162px, var(--timber-d) 162px 216px,
        var(--timber-a) 216px 270px);
  }
  .chalkboard {
    position: absolute; left: 40px; top: 36px; width: 380px; height: 220px;
  }
  .brand {
    position: absolute; left: 40px; top: 62px; width: 380px;
    text-align: center; color: var(--pink);
    font-family: "Lobster", cursive; font-weight: 400;
  }
  .brand-name { display: block; font-size: 48px; line-height: 1; }
  .brand-sub { display: block; font-size: 22px; line-height: 1.3; margin-top: 4px; }
  .phone {
    position: absolute; left: 150px; top: 172px; width: 160px; height: 26px;
    border-radius: 13px; background: var(--pink-deep);
    color: var(--cream); font-family: "Roboto", sans-serif; font-weight: 500;
    font-size: 14px; letter-spacing: .5px;
    display: flex; align-items: center; justify-content: center;
  }
  .cake-art {
    position: absolute; left: 378px; top: 110px; width: 100px; height: 160px;
    border-radius: 12px;
    background: linear-gradient(180deg, #f2b9bf 0%, var(--pink) 60%, var(--pink-deep) 100%);
  }

  /* Back */
  .card-back { display: flex; }
  .photo-tiered {
    width: 60%; height: 100%;
    background: linear-gradient(180deg, var(--photo-warm-b) 0%, #d8b48c 40%, var(--photo-warm-a) 75%, #8b5a3c 100%);
  }
  .photo-wedding {
    width: 40%; height: 100%;
    background: linear-gradient(180deg, var(--photo-cream-b) 0%, #c9b99a 35%, var(--photo-cream-a) 70%, #f3efcf 100%);
  }
  .statement {
    position: absolute; left: 0; right: 0; top: 186px; height: 44px;
    background: rgba(251,248,241,.72);
    display: flex; align-items: center; justify-content: center;
    font-family: "Dancing Script", cursive; font-weight: 500;
    font-size: 21px; color: var(--ink);
  }
</style>
</head>
<body>
<main class="canvas">
  <section class="card card-front" aria-label="Card front">
    <svg class="chalkboard" viewBox="0 0 380 220" aria-hidden="true">
      <path d="M30 0 H350 Q350 30 380 30 V190 Q350 190 350 220 H30 Q30 190 0 190 V30 Q30 30 30 0 Z" fill="var(--chalk)"/>
      <path d="M38 10 H342 Q344 38 370 40 V180 Q344 182 342 210 H38 Q36 182 10 180 V40 Q36 38 38 10 Z" fill="none" stroke="var(--chalk-line)" stroke-width="2"/>
    </svg>
    <h1 class="brand">
      <span class="brand-name">Marigold's</span>
      <span class="brand-sub">Sugarloft Bakes</span>
    </h1>
    <div class="phone">0417 382 254</div>
    <div class="cake-art" role="img" aria-label="Illustration of a pink three-tier cake with candles on a cake stand"></div>
  </section>

  <section class="card card-back" aria-label="Card back">
    <div class="photo-tiered" role="img" aria-label="Photo of a tiered birthday cake with a globe on top and ribbon banners"></div>
    <div class="photo-wedding" role="img" aria-label="Photo of a cream wedding cake with flowers and a heart topper"></div>
    <p class="statement">Specialising in delectable treats for all your special occasions</p>
  </section>
</main>
</body>
</html>
```